Business Card Design Needed for Landscaping & Trail Building Company

We need a business card for our landscaping and trail-building business using our current artwork (attached). We build mountain bike trails and pump tacks along with our base business - landscaping - which is primarily earth moving, machine work, concreting, retaining walls, paths, etc. for commercial and residential customers. We want a design that is professional, sleek, and earthy. We like clean, open space (i.e. logo artwork only, on one side, with pertinent information on the back) and a somewhat ambiguous look considering our varied clientele between the trail work and the landscape work.

Target Market(s)

Ski resort executives. government employees (rangers, council members, etc), average homeowner, other tradies, builders, etc.

Contact Information for Business Card

Must include the following:
employee name: Marcus
mobile number: 0491 637 215
email: marcus@brellowgrounds.com.au
website: brellowgrounds.com.au
ABN: 58 314 902 667
QBCC: 27846159
^This is the Queensland Building & Construction Commission license number, a requirement to be displayed on promotional material for our state
Description of services: "Residential and commercial landscaping, minor earth works and trail building"

Font styles to use
Serif

Colors
ffc214
9bcb3c
333333
0355a3

Requirements
Must have
• Please see "Business Card Details" as these are all the pieces of information required to be on there. This will be a slim card, so the final size needs to be 45mm x 90mm, landscape perspective.
• I will include the requirements of our printer below:
• File Format
• PDF files
• CMYK colour
• 300dpi resolution minimum
• Fonts converted to outlines or flattened
• Resolution
• Images such as photos in your artwork must have a minimum resolution of 300dpi. Images that have a lower resolution may print pixelated or fuzzy. Images taken from the internet often have a resolution of only 72dpi and will very rarely print very well.
• Correct Colour
• Digital printing uses a CMYK colour format (Cyan, Magenta, Yellow and Black). The colours on your screen are RGB colours (Red, Green, Blue).
• Some RGB colours that appear on your screen can not be printed in CMYK. You must be careful when selecting colours for your printing, as some colours will print "dull" when compared to your computer screen.
• Programs such as Adobe Photoshop and Adobe Illustrator can convert all colours to CMYK. Programs such as Microsoft Word can not, so you must manually select colours which are not at risk.
• Fonts
• You may choose to select only common fonts such as "Arial" and "Times New Roman", or you can "embed" the fonts when saving your artwork. Preferably fonts in your artwork need to be "converted to outlines" or "flattened" into a graphic. This will eliminate the chance of fonts not displaying correctly and not printing the way you intended.
• Business Card Artwork Size
• 94mm x 59mm (including 2mm bleed)
• Artwork Bleeds - IMPORTANT!
• Your artwork needs to be a certain size to print correctly. For business cards it is 94mmx59mm. Part of this size is what we call the "bleed" which will be trimmed off. The bleed area is 2mm on each side. In addition to the bleed area outside the cut line, we strongly recommend making another internal margin as the cut line can vary in location.
Nice to have
• We will have a print run of two designs, one with my details (Dianne) and one with Marcus's.
• (I like the idea of the name being larger than everything else, jumping out)
• The background colours we are interested in: very dark navy blue (almost black), fluorescent orange and green (same colour palette as our current artwork), and possibly black. The rest of the colour theming should match our current artwork. We will likely be printing these out in matte/soft finish with a gloss spot accent on the logo.
• I have attached the front/back of an example business card that we both like the look of.
• As a side note, we are open to creative designs that design outside of our specified preferences, as we have been blown away in the past by the creativity of designers.

```html
<!DOCTYPE html>
<html lang="en">
<head>
<meta charset="utf-8">
<title>Brellow Grounds – Business Cards</title>
<link rel="stylesheet" href="https://fonts.googleapis.com/css2?family=Cinzel:wght@600&family=Tinos:wght@400;700&family=Arimo&display=swap">
<style>
  :root {
    --navy-deep: #141a2f;
    --navy-blue: #0b4b8c;
    --orange: #f0932b;
    --green: #8cc043;
    --white: #ffffff;
    --ink: #555555;
    --label: #222222;
    --rule-light: #cfd3da;
    --rule-dark: #8a8f99;
  }
  * { box-sizing: border-box; margin: 0; padding: 0; }
  html, body { width: 1126px; height: 1200px; overflow: hidden; background: var(--white); }
  body { position: relative; font-family: "Tinos", "Times New Roman", serif; }

  .section-label {
    position: absolute; left: 0; width: 1126px; text-align: center;
    font-family: "Arimo", Arial, sans-serif; font-size: 19px; color: var(--label);
  }
  .section-label--front { top: -3px; }
  .section-label--back { top: 318px; }

  .card {
    position: absolute; width: 552px; height: 276px; overflow: hidden;
  }
  .card--gradient { background: linear-gradient(160deg, var(--navy-deep) 45%, var(--navy-blue) 100%); }
  .card--dark { background: var(--navy-deep); }
  .card--light { background: var(--white); border: 1px solid var(--rule-dark); }

  .col-left { left: 0; }
  .col-right { left: 574px; }
  .row-front { top: 29px; }
  .row-1 { top: 346px; }
  .row-2 { top: 634px; }
  .row-3 { top: 922px; }

  /* front */
  .brand { position: absolute; left: 58px; top: 54px; display: flex; align-items: center; gap: 14px; }
  .brand__mark { width: 100px; height: 100px; border-radius: 50%; background: var(--green); }
  .brand__name {
    font-family: "Tinos", serif; font-weight: 700; font-size: 38px; color: var(--green);
    letter-spacing: 1px;
  }
  .tagline {
    position: absolute; left: 0; width: 552px; top: 198px; text-align: center;
    font-family: "Cinzel", "Times New Roman", serif; font-weight: 600; font-size: 14.5px;
    line-height: 22px; letter-spacing: 1.6px; color: var(--white);
  }

  /* back */
  .mark {
    position: absolute; left: 95px; top: 78px; width: 102px; height: 102px;
    border-radius: 50%; background: var(--green);
  }
  .divider { position: absolute; left: 228px; top: 66px; width: 1px; height: 128px; background: var(--rule-dark); }
  .card--light .divider { background: var(--ink); }
  .person-name {
    position: absolute; left: 259px; top: 66px; font-weight: 700; font-size: 33px; color: var(--orange);
  }
  .contact { position: absolute; left: 255px; top: 111px; list-style: none; }
  .contact li {
    display: flex; align-items: center; height: 24px;
    font-size: 18.5px; color: var(--white);
  }
  .card--light .contact li { color: var(--ink); }
  .contact svg { width: 14px; height: 14px; margin-right: 14px; flex: none; }
  .legal {
    position: absolute; left: 397px; top: 224px; font-size: 11.5px; line-height: 14.5px; color: var(--white);
  }
  .card--light .legal { color: var(--ink); }
</style>
</head>
<body>

<div class="section-label section-label--front">Front</div>

<section class="card card--gradient col-left row-front">
  <div class="brand"><span class="brand__mark"></span><span class="brand__name">BRELLOW GROUNDS</span></div>
  <p class="tagline">Residential and commercial landscaping,<br>minor earth works and trail building</p>
</section>
<section class="card card--gradient col-right row-front">
  <div class="brand"><span class="brand__mark"></span><span class="brand__name">BRELLOW GROUNDS</span></div>
  <p class="tagline">Residential and commercial landscaping,<br>minor earth works and trail building</p>
</section>

<div class="section-label section-label--back">Back</div>

<!-- reusable icon symbols -->
<svg width="0" height="0" style="position:absolute">
  <symbol id="icon-phone" viewBox="0 0 14 14"><rect x="3" y="0.8" width="8" height="12.4" rx="1.8" fill="none" stroke="#8cc043" stroke-width="1.6"/><rect x="5.5" y="10" width="3" height="1.2" fill="#8cc043"/></symbol>
  <symbol id="icon-mail" viewBox="0 0 14 14"><rect x="0.5" y="2.5" width="13" height="9" fill="#8cc043"/><path d="M0.8 3 L7 8 L13.2 3 M0.8 11 L5 7 M13.2 11 L9 7" fill="none" stroke="#141a2f" stroke-width="0.9"/></symbol>
  <symbol id="icon-web" viewBox="0 0 14 14"><circle cx="7" cy="7" r="6" fill="none" stroke="#8cc043" stroke-width="1.4"/><ellipse cx="7" cy="7" rx="2.6" ry="6" fill="none" stroke="#8cc043" stroke-width="1.1"/><path d="M1 7 H13 M2 4 H12 M2 10 H12" stroke="#8cc043" stroke-width="1.1"/></symbol>
</svg>

<!-- row 1 -->
<section class="card card--gradient col-left row-1">
  <span class="mark" role="img" aria-label="Brellow Grounds mark"></span><span class="divider"></span>
  <h2 class="person-name">Marcus</h2>
  <ul class="contact">
    <li><svg><use href="#icon-phone"/></svg>0491 637 215</li>
    <li><svg><use href="#icon-mail"/></svg>marcus@brellowgrounds.com.au</li>
    <li><svg><use href="#icon-web"/></svg>brellowgrounds.com.au</li>
  </ul>
  <p class="legal">ABN: 58 314 902 667<br>QBCC: 27846159</p>
</section>
<section class="card card--gradient col-right row-1">
  <span class="mark" role="img" aria-label="Brellow Grounds mark"></span><span class="divider"></span>
  <h2 class="person-name">Dianne</h2>
  <ul class="contact">
    <li><svg><use href="#icon-phone"/></svg>0497 812 340</li>
    <li><svg><use href="#icon-mail"/></svg>dianne@brellowgrounds.com.au</li>
    <li><svg><use href="#icon-web"/></svg>brellowgrounds.com.au</li>
  </ul>
  <p class="legal">ABN: 58 314 902 667<br>QBCC: 27846159</p>
</section>

<!-- row 2 -->
<section class="card card--dark col-left row-2">
  <span class="mark" role="img" aria-label="Brellow Grounds mark"></span><span class="divider"></span>
  <h2 class="person-name">Marcus</h2>
  <ul class="contact">
    <li><svg><use href="#icon-phone"/></svg>0491 637 215</li>
    <li><svg><use href="#icon-mail"/></svg>marcus@brellowgrounds.com.au</li>
    <li><svg><use href="#icon-web"/></svg>brellowgrounds.com.au</li>
  </ul>
  <p class="legal">ABN: 58 314 902 667<br>QBCC: 27846159</p>
</section>
<section class="card card--dark col-right row-2">
  <span class="mark" role="img" aria-label="Brellow Grounds mark"></span><span class="divider"></span>
  <h2 class="person-name">Dianne</h2>
  <ul class="contact">
    <li><svg><use href="#icon-phone"/></svg>0497 812 340</li>
    <li><svg><use href="#icon-mail"/></svg>dianne@brellowgrounds.com.au</li>
    <li><svg><use href="#icon-web"/></svg>brellowgrounds.com.au</li>
  </ul>
  <p class="legal">ABN: 58 314 902 667<br>QBCC: 27846159</p>
</section>

<!-- row 3 -->
<section class="card card--light col-left row-3">
  <span class="mark" role="img" aria-label="Brellow Grounds mark"></span><span class="divider"></span>
  <h2 class="person-name">Marcus</h2>
  <ul class="contact">
    <li><svg><use href="#icon-phone"/></svg>0491 637 215</li>
    <li><svg><use href="#icon-mail"/></svg>marcus@brellowgrounds.com.au</li>
    <li><svg><use href="#icon-web"/></svg>brellowgrounds.com.au</li>
  </ul>
  <p class="legal">ABN: 58 314 902 667<br>QBCC: 27846159</p>
</section>
<section class="card card--light col-right row-3">
  <span class="mark" role="img" aria-label="Brellow Grounds mark"></span><span class="divider"></span>
  <h2 class="person-name">Dianne</h2>
  <ul class="contact">
    <li><svg><use href="#icon-phone"/></svg>0497 812 340</li>
    <li><svg><use href="#icon-mail"/></svg>dianne@brellowgrounds.com.au</li>
    <li><svg><use href="#icon-web"/></svg>brellowgrounds.com.au</li>
  </ul>
  <p class="legal">ABN: 58 314 902 667<br>QBCC: 27846159</p>
</section>

</body>
</html>
```